Need a webinar banner promo to place on social media

We are organise a series of webinars in coming months.

We need a webinar banner design to be posted on Facebook and linkedin. The banner is for our webinar titled: Ways to Debut a Novel with Sparkle and Flair.

our website is www.quillmarket.com.au

there is a link on the website to the webinar registration for your reference.

```html
<!DOCTYPE html>
<html lang="en">
<head>
<meta charset="utf-8">
<title>Ways to Debut a Novel with Sparkle and Flair – Free Webinar</title>
<link href="https://fonts.googleapis.com/css2?family=Montserrat:wght@400;500;700;800&display=swap" rel="stylesheet">
<style>
  :root {
    --navy: #15304f;
    --navy-text: #152f52;
    --gold: #b3862c;
    --gold-light: #e9c85a;
    --yellow: #d9c457;
    --yellow-deep: #a89440;
    --steel: #4f6a89;
    --white: #ffffff;
  }
  * { margin: 0; padding: 0; box-sizing: border-box; }
  html, body { width: 1200px; height: 618px; overflow: hidden; background: var(--white); }
  .banner {
    position: relative; width: 1200px; height: 618px; overflow: hidden;
    font-family: "Montserrat", Arial, sans-serif; color: var(--navy-text); background: var(--white);
  }
  .banner-shapes { position: absolute; inset: 0; }
  .headline {
    position: absolute; top: 46px; left: 0; width: 100%; text-align: center;
    font-size: 47px; line-height: 62px; letter-spacing: 0.5px; text-transform: uppercase;
  }
  .headline .light { font-weight: 400; }
  .headline .strong { font-weight: 800; }
  .brand {
    position: absolute; left: 40px; width: 440px; top: 268px; text-align: center;
    color: var(--gold); font-weight: 800; text-transform: uppercase; line-height: 1;
  }
  .brand-main { display: block; font-size: 82px; letter-spacing: -1px; }
  .brand-sub { display: block; font-size: 96px; margin-top: 8px; letter-spacing: 4px; }
  .webinar-tab {
    position: absolute; left: 724px; top: 193px; width: 312px; height: 48px;
    background: var(--white); border-radius: 0 0 10px 10px;
    color: var(--gold); font-weight: 800; font-size: 31px; text-align: center; line-height: 46px;
  }
  .rule { position: absolute; left: 663px; width: 421px; height: 1px; background: rgba(255,255,255,0.85); }
  .rule-top { top: 276px; }
  .rule-bottom { top: 439px; }
  .date-day {
    position: absolute; left: 655px; top: 278px; font-weight: 800; font-size: 150px;
    line-height: 160px; letter-spacing: -8px;
  }
  .date-month, .date-year { position: absolute; left: 828px; font-weight: 800; font-size: 60px; line-height: 60px; }
  .date-month { top: 296px; }
  .date-year { top: 366px; }
  .event-time { position: absolute; left: 663px; top: 462px; font-weight: 800; font-size: 33px; line-height: 44px; white-space: nowrap; }
  .register-label { position: absolute; left: 617px; top: 555px; font-weight: 500; font-size: 27px; line-height: 34px; }
  .register-link {
    position: absolute; left: 815px; top: 551px; width: 329px; height: 44px; border-radius: 0 22px 22px 0;
    background: linear-gradient(90deg, var(--gold), var(--gold-light));
    font-weight: 800; font-size: 27px; line-height: 44px; text-align: center; color: var(--navy-text);
  }
</style>
</head>
<body>
<main class="banner">
  <svg class="banner-shapes" width="1200" height="618" viewBox="0 0 1200 618" aria-hidden="false">
    <defs>
      <linearGradient id="photo-tone" x1="0" y1="0" x2="1" y2="0">
        <stop offset="0" stop-color="#a8973f"/>
        <stop offset="0.5" stop-color="#c9b450"/>
        <stop offset="1" stop-color="#e3d064"/>
      </linearGradient>
    </defs>
    <rect class="photo-area" x="520" y="193" width="680" height="335" fill="url(#photo-tone)" role="img" aria-label="Blurred photograph of an author speaking to an audience at a book launch, tinted gold"/>
    <polygon class="steel-stripe" points="571,193 591,193 543,618 522,618" fill="var(--steel)" opacity="0.9"/>
    <polygon class="navy-panel" points="0,193 571,193 522,618 0,618" fill="var(--navy)"/>
  </svg>

  <h1 class="headline">
    <span class="light">Ways to Debut</span> <span class="strong">a Novel</span><br>
    <span class="strong">with Sparkle and Flair.</span>
  </h1>

  <div class="brand">
    <span class="brand-main">Novella</span>
    <span class="brand-sub">Fair</span>
  </div>

  <div class="webinar-tab">FREE WEBINAR</div>
  <div class="rule rule-top"></div>
  <div class="date-day">15</div>
  <div class="date-month">MARCH</div>
  <div class="date-year">2023</div>
  <div class="rule rule-bottom"></div>
  <div class="event-time">7:00 PM – 8:00 PM AEDT</div>

  <div class="register-label">Register Now</div>
  <div class="register-link">quillmarket.com.au</div>
</main>
</body>
</html>
```